依頼詳細
シンプルかつスタイリッシュで、落ち着いたデザインを希望します。弊社イメージカラーはオレンジですが、建物との統一性を持たせたカラー(紺色:写真参照)のほうが良いかと思っています。(オレンジを使用していただいても結構です)
サイズや表記内容等は「記載項目」をご覧ください。
記載項目
ミナセリアルティ株式会社
ミナセリーガル事務所またはミナセリーガル行政書士|土地家屋調査士事務所(バランス等考慮し、どちらかを選択)は必須ですが、電話番号は必要ありません。
また、ロゴマークも必須ですが、マークの選択はお任せします。(添付ファイル参照)
また、事業内容については参考に名刺を添付しますが、多くの情報を入れることは望みません。事業所名をミナセリーガル事務所とする場合は、行政書士及び土地家屋調査士を事業内容としていただいても結構です。
寸法につきましては、添付ファイルをご確認ください。

希望イメージ
シンプル 複雑
単色 カラフル
暗い 明るい
日常 高級
遊び心 厳粛
未来的 伝統的
女性的 男性的
希望する色
事務所看板のため、建物と統一性のあるものにしたいです
納品ファイル
• イラストレーター形式 (.ai)
補足説明
事業内容は必ずしも記載しなければならないものではありません。(どちらでもよいです)
■ 選んだ理由

「シンプルでスタイリッシュ」の希望を見事に叶えていただきました。
中でもロゴの配置が絶妙で、色合いも素晴らしかったです。

■ 提案者全員のお礼・コメント

この度は弊社コンペにご参加いただきまして、誠にありがとうございました。
レベルが高く秀逸な作品が多いため選定に悩みましたが、嬉しい悲鳴で選定を楽しませていただきました。
今後も業務拡大を目指しておりますので、折に触れコンペを開催させていただくつもりですので、引き続きよろしくお願いいたします。

```html
<!DOCTYPE html>
<html lang="ja">
<head>
<meta charset="utf-8">
<title>ミナセリアルティ 看板デザイン</title>
<link rel="stylesheet" href="https://fonts.googleapis.com/css2?family=Noto+Serif+JP:wght@500;600&family=Cormorant+Garamond:wght@500&family=Montserrat:wght@700&display=swap">
<style>
  :root {
    --bg: #e8e8e9;
    --panel-white: #ffffff;
    --panel-edge: #d6d6d8;
    --navy: #364667;
    --ink: #4a4a4a;
    --orange: #ee7d1c;
    --text-light: #ffffff;
    --label: #222222;
    --leg: #f4f4f4;
  }
  * { margin: 0; padding: 0; box-sizing: border-box; }
  html, body { width: 846px; height: 1200px; overflow: hidden; }
  body { background: var(--bg); position: relative; }

  .sign {
    position: absolute;
    left: 234px; top: 34px;
    width: 378px; height: 1089px;
    border: 1px solid var(--panel-edge);
    background: var(--panel-white);
  }
  .sign__brand {
    position: absolute; left: 0; top: 0;
    width: 100%; height: 539px;
  }
  .brand__dot {
    position: absolute; left: 144px; top: 210px;
    width: 90px; height: 90px; border-radius: 50%;
    background: var(--orange);
  }
  .brand__name {
    position: absolute; left: 0; right: 0; top: 470px;
    text-align: center;
    font-family: "Cormorant Garamond", serif;
    font-weight: 500; font-size: 34px; letter-spacing: 2px;
    color: var(--ink);
  }
  .sign__offices {
    position: absolute; left: 0; top: 539px;
    width: 100%; height: 550px;
    background: var(--navy);
  }
  .office {
    position: absolute; left: 0; right: 0;
    text-align: center; color: var(--text-light);
    font-family: "Noto Serif JP", serif;
    font-weight: 600; font-size: 28px; line-height: 37px;
  }
  .office::after {
    content: ""; display: block;
    width: 208px; height: 4px; margin: 18px auto 0;
    background: var(--text-light);
  }
  .office--realty { top: 54px; }
  .office--legal  { top: 228px; }
  .office--survey { top: 400px; }

  .sign__leg {
    position: absolute; top: 1123px;
    width: 16px; height: 34px;
    background: var(--leg);
    border: 1px solid var(--panel-edge); border-top: none;
  }
  .sign__leg--left { left: 250px; }
  .sign__leg--right { left: 580px; }

  .sheet-label, .sheet-page {
    position: absolute; top: 1160px;
    font-family: "Montserrat", sans-serif; font-weight: 700;
    color: var(--label);
  }
  .sheet-label { left: 28px; font-size: 14px; letter-spacing: 3px; }
  .sheet-page { right: 24px; font-size: 13px; font-weight: 500; color: #666; }
</style>
</head>
<body>
  <div class="sign">
    <div class="sign__brand">
      <span class="brand__dot" aria-hidden="true"></span>
      <p class="brand__name">MINASE REALTY</p>
    </div>
    <div class="sign__offices">
      <p class="office office--realty">ミナセリアルティ<br>株式会社</p>
      <p class="office office--legal">ミナセリーガル<br>行政書士</p>
      <p class="office office--survey">土地家屋<br>調査士事務所</p>
    </div>
  </div>
  <div class="sign__leg sign__leg--left"></div>
  <div class="sign__leg sign__leg--right"></div>

  <p class="sheet-label">DESIGN C</p>
  <p class="sheet-page">1/10</p>
</body>
</html>
```